Harrowby Lending Hard Money Lender

We are looking for this flyer to be redesigned. We would like it to be even more simple than the attached design. No photos, no exclamation points, a 3-4 color palate maximum. We would do not want any graphics around the "Harrowby Lending" logo.

```html
<!DOCTYPE html>
<html lang="en">
<head>
<meta charset="UTF-8">
<title>Harrowby Lending – Hard Money Loans Flyer</title>
<link href="https://fonts.googleapis.com/css2?family=Alegreya+Sans:wght@400;700&family=Tenor+Sans&family=Tinos:wght@700&display=swap" rel="stylesheet">
<style>
  :root {
    --page-bg: #142848;
    --navy: #15233f;
    --royal: #063d80;
    --paper: #e4e5ea;
    --ink: #1a1d2a;
    --phone-blue: #0b3d7e;
    --white: #ffffff;
    --silver-light: #f2f3f5;
    --silver-dark: #a9acb3;
  }
  * { margin: 0; padding: 0; box-sizing: border-box; }
  html, body {
    width: 1150px;
    height: 1200px;
    overflow: hidden;
    background: var(--page-bg);
  }
  .flyer {
    position: absolute;
    left: 163px;
    top: 60px;
    width: 823px;
    height: 1080px;
    display: flex;
    flex-direction: column;
    font-family: "Alegreya Sans", sans-serif;
  }
  .brand-band {
    position: relative;
    height: 340px;
    background: var(--navy);
  }
  .brand-name {
    position: absolute;
    left: 0;
    right: 0;
    top: 128px;
    text-align: center;
    font-family: "Tenor Sans", sans-serif;
    font-size: 56px;
    letter-spacing: 2px;
    color: var(--white);
  }
  .offer-band {
    position: relative;
    height: 352px;
    background: var(--royal);
    color: var(--white);
  }
  .offer-title {
    position: absolute;
    left: 67px;
    top: 88px;
    font-family: "Alegreya Sans", sans-serif;
    font-weight: 700;
    font-size: 50px;
    line-height: 46px;
    letter-spacing: 0.5px;
  }
  .rate-pill {
    position: absolute;
    left: 60px;
    top: 195px;
    width: 328px;
    height: 49px;
    border-radius: 25px;
    background: linear-gradient(180deg, var(--silver-light) 0%, #d2d4d9 55%, var(--silver-dark) 100%);
    color: var(--royal);
    font-family: "Tenor Sans", sans-serif;
    font-size: 36px;
    line-height: 49px;
    padding-left: 30px;
  }
  .loan-types {
    position: absolute;
    left: 480px;
    top: 98px;
    list-style: none;
  }
  .loan-types li {
    display: flex;
    align-items: center;
    height: 56.5px;
    font-weight: 700;
    font-size: 28px;
  }
  .tick {
    width: 28px;
    height: 24px;
    margin-right: 12px;
    flex: none;
  }
  .contact-band {
    position: relative;
    height: 358px;
    background: var(--paper);
    color: var(--ink);
  }
  .benefits {
    position: absolute;
    left: 62px;
    top: 42px;
    list-style: none;
    font-size: 24px;
    line-height: 33px;
  }
  .benefits strong { font-weight: 700; }
  .phone {
    position: absolute;
    left: 60px;
    top: 150px;
    font-family: "Tinos", serif;
    font-weight: 700;
    font-size: 76px;
    color: var(--phone-blue);
    letter-spacing: 0.5px;
  }
  .web-links {
    position: absolute;
    left: 62px;
    top: 252px;
    font-size: 25px;
    line-height: 34px;
  }
  .footer-band {
    height: 30px;
    background: var(--navy);
  }
</style>
</head>
<body>
  <main class="flyer">
    <header class="brand-band">
      <div class="brand-name">HARROWBY LENDING</div>
    </header>

    <section class="offer-band">
      <h1 class="offer-title">HARD MONEY<br>LOANS</h1>
      <div class="rate-pill">Rates From 8%</div>
      <ul class="loan-types">
        <li><svg class="tick" viewBox="0 0 28 24" aria-hidden="true"><path d="M2 13 L10 21 L26 3" fill="none" stroke="#ffffff" stroke-width="5" stroke-linecap="round" stroke-linejoin="round"/></svg>Fix &amp; Flip Loans</li>
        <li><svg class="tick" viewBox="0 0 28 24" aria-hidden="true"><path d="M2 13 L10 21 L26 3" fill="none" stroke="#ffffff" stroke-width="5" stroke-linecap="round" stroke-linejoin="round"/></svg>Commercial Loans</li>
        <li><svg class="tick" viewBox="0 0 28 24" aria-hidden="true"><path d="M2 13 L10 21 L26 3" fill="none" stroke="#ffffff" stroke-width="5" stroke-linecap="round" stroke-linejoin="round"/></svg>Hard Money Loans</li>
      </ul>
    </section>

    <section class="contact-band">
      <ul class="benefits">
        <li><strong>Same-Day Approval</strong></li>
        <li><strong>No Processing, Appraisal, or Extra Fees</strong></li>
        <li><strong>100% Financing</strong> (w/ Additional Collateral)</li>
      </ul>
      <div class="phone">303.555.0142</div>
      <div class="web-links">
        <div>loans@harrowbylending.com</div>
        <div>http://harrowbylending.com</div>
      </div>
    </section>

    <footer class="footer-band"></footer>
  </main>
</body>
</html>
```